Inspirational Quotes Poster Set

Braxlune is a stylish coworking space, which has a design-oriented vintage look from the 60's with an industrial touch (www.braxlune-example.com) Braxlune Quote Poster Set of 16 posters. The poster should be typo oriented and rather simple. Reflecting a bit the clean billboard design from the sixties. Minimal / simple graphical elements

Target Market(s)

Startups and Entrepreneurs

Industry/Entity Type

Startup

Font styles to use
Sans Serif

Colors

Designer to choose colors to be used in the design.

Requirements
Must have
• Posters need to be on and very stylish

```html
<!DOCTYPE html>
<html lang="en">
<head>
<meta charset="utf-8">
<title>Braxlune Quote Poster – Going Fast Enough</title>
<link rel="stylesheet" href="https://fonts.googleapis.com/css2?family=Space+Grotesk:wght@500;700&display=swap">
<style>
  :root {
    --paper: #ffffff;
    --teal: #14a29a;
    --ink-light: #ffffff;
  }
  html, body {
    margin: 0;
    padding: 0;
    overflow: hidden;
    background: var(--paper);
  }
  .poster {
    display: block;
    width: 801px;
    height: 1200px;
  }
  .poster-bg { fill: var(--paper); }
  .poster-band { fill: var(--teal); }
  .quote-lead {
    font-family: "Space Grotesk", sans-serif;
    font-weight: 700;
    font-size: 58px;
    letter-spacing: -2.5px;
    fill: var(--teal);
  }
  .quote-main {
    font-family: "Space Grotesk", sans-serif;
    font-weight: 700;
    font-size: 100px;
    letter-spacing: -4.5px;
    fill: var(--ink-light);
  }
  .attribution {
    font-family: "Space Grotesk", sans-serif;
    font-weight: 700;
    font-size: 21px;
    letter-spacing: -0.8px;
    fill: var(--ink-light);
  }
  .brand-name {
    font-family: "Space Grotesk", sans-serif;
    font-weight: 700;
    font-size: 40px;
    letter-spacing: -1.5px;
    fill: var(--ink-light);
  }
</style>
</head>
<body>
<svg class="poster" viewBox="0 0 801 1200" xmlns="http://www.w3.org/2000/svg">
  <defs>
    <linearGradient id="flag-tone" x1="0" y1="0" x2="1" y2="1">
      <stop offset="0" stop-color="#ffffff" stop-opacity="0.35"/>
      <stop offset="1" stop-color="#ffffff" stop-opacity="0.12"/>
    </linearGradient>
  </defs>

  <rect class="poster-bg" x="0" y="0" width="801" height="1200"/>
  <rect class="poster-band" x="0" y="255" width="801" height="945"/>

  <rect class="flag-artwork" x="238" y="445" width="563" height="580" fill="url(#flag-tone)"
        role="img" aria-label="Waving chequered racing flag on a pole"/>

  <g class="quote">
    <text class="quote-lead" x="72" y="186">if everything seems</text>
    <text class="quote-lead" x="72" y="244">under control,</text>
    <text class="quote-main" x="74" y="326">you’re</text>
    <text class="quote-main" x="56" y="424">just not</text>
    <text class="quote-main" x="78" y="522">going fast</text>
    <text class="quote-main" x="78" y="621">enough</text>
  </g>

  <g class="quote-attribution">
    <text class="attribution" x="71" y="1039">Marco Vellani,</text>
    <text class="attribution" x="71" y="1067">Legendary Race Car Driver</text>
  </g>

  <text class="brand-name" x="401" y="1142" text-anchor="middle">braxlune</text>
</svg>
</body>
</html>
```